exclusive beauty spa needs a poster design

Poster design needed to attract more customers to business. We specialise in massages, slimming and full day spa packages. We are only one of a few spa's selling the exclusive "Lulu Vexa" range and this is currently our best received product. We want the people to know that we are also on Facebook (BriarleaSpa) & Twitter (@KentivaDaySpa). Our colors that we mainly use is green & blue to give it an earthy tone. Poster size should be 1960mm high by 1360mm wide. visual size is 1800mm high by 1200mm wide. bleed is 160mm basicly.

Target Market(s)

Females from age group 16 right up to 60.

Industry/Entity Type

Business

Requirements
Must have
• Must use company logo and have Facebook Logo on poster

```html
<!DOCTYPE html>
<html lang="en">
<head>
<meta charset="utf-8">
<title>Kentiva Day Spa – Poster</title>
<link rel="stylesheet" href="https://fonts.googleapis.com/css2?family=PT+Sans:ital,wght@0,400;0,700;1,400;1,700&display=swap">
<style>
  :root {
    --page: #e9e9e6;
    --paper: #ffffff;
    --pink: #e2307c;
    --pink-band: rgba(236, 150, 185, 0.28);
    --green: #8fae1b;
    --green-light: #c9d66a;
    --green-pale: #eef2c8;
    --blue: #3f9fd3;
    --text: #4a4a4a;
    --skin: #d9a88a;
    --skin-light: #efd2bf;
  }
  * { margin: 0; padding: 0; box-sizing: border-box; }
  html, body { width: 1200px; height: 1200px; overflow: hidden; background: var(--page); }
  body { font-family: "PT Sans", Arial, sans-serif; color: var(--text); }

  .poster {
    position: absolute; left: 236px; top: 39px;
    width: 728px; height: 1122px;
    background: var(--paper); overflow: hidden;
  }
  .poster__layer { position: absolute; inset: 0; }

  .brand { position: absolute; right: 60px; top: 88px; text-align: right; }
  .brand__name { font-size: 36px; font-weight: 700; color: var(--green); line-height: 1; }
  .brand__tagline { font-size: 15px; font-style: italic; color: var(--blue); margin-top: 6px; }

  .intro { position: absolute; right: 52px; top: 308px; font-size: 27px; color: var(--pink); }
  .headline {
    position: absolute; right: 52px; top: 368px; text-align: right;
    font-size: 64px; font-weight: 700; line-height: 1.08; color: var(--pink);
  }
  .offer {
    position: absolute; left: 290px; right: 52px; top: 548px;
    font-size: 16px; line-height: 1.4; color: var(--text);
  }
  .closing { position: absolute; right: 52px; top: 632px; font-size: 32px; font-weight: 700; color: var(--pink); }

  .services { position: absolute; left: 60px; top: 735px; }
  .services__title { font-size: 25px; font-style: italic; color: var(--green); margin-bottom: 8px; }
  .services__list { list-style: none; }
  .services__item {
    display: flex; align-items: center; gap: 8px;
    font-size: 23px; font-style: italic; color: var(--green); line-height: 1.3;
  }
  .services__item svg { width: 16px; height: 16px; flex: none; }

  .address {
    position: absolute; right: 52px; top: 905px; text-align: right;
    font-size: 12.5px; line-height: 1.45; color: var(--text);
  }
  .social { position: absolute; left: 60px; top: 1038px; font-size: 12px; color: #ffffff; }
  .social__links { display: flex; gap: 16px; margin-top: 4px; }
  .social__link { display: flex; align-items: center; gap: 5px; font-weight: 700; }
  .social__dot { width: 12px; height: 12px; border-radius: 50%; background: var(--blue); }
  .notice {
    position: absolute; right: 52px; top: 1038px; width: 250px; text-align: right;
    font-size: 10.5px; line-height: 1.35; color: #ffffff;
  }
</style>
</head>
<body>
  <main class="poster">
    <svg class="poster__layer" viewBox="0 0 728 1122" width="728" height="1122" aria-hidden="false">
      <defs>
        <linearGradient id="photoTone" x1="0" y1="0" x2="1" y2="0">
          <stop offset="0" stop-color="var(--skin)"/>
          <stop offset="0.55" stop-color="var(--skin-light)"/>
          <stop offset="1" stop-color="#ffffff" stop-opacity="0"/>
        </linearGradient>
        <linearGradient id="photoFade" x1="0" y1="0" x2="0" y2="1">
          <stop offset="0.6" stop-color="#ffffff" stop-opacity="0"/>
          <stop offset="1" stop-color="#ffffff" stop-opacity="1"/>
        </linearGradient>
        <linearGradient id="swoosh" x1="0" y1="0" x2="0" y2="1">
          <stop offset="0" stop-color="var(--green-light)"/>
          <stop offset="1" stop-color="var(--green)"/>
        </linearGradient>
      </defs>

      <g role="img" aria-label="Photo of a woman lying face down on a massage bed with hot stones along her spine, pink petals scattered around">
        <rect class="photo" x="0" y="0" width="480" height="800" fill="url(#photoTone)"/>
        <rect x="0" y="0" width="480" height="800" fill="url(#photoFade)"/>
      </g>

      <rect class="headline-band" x="0" y="355" width="728" height="160" fill="var(--pink-band)"/>

      <path class="swoosh swoosh--pale" d="M0 760 C200 830 480 840 728 790 L728 1122 L0 1122 Z" fill="var(--green-pale)"/>
      <path class="swoosh swoosh--main" d="M0 900 C220 990 500 1000 728 950 L728 1122 L0 1122 Z" fill="url(#swoosh)"/>
    </svg>

    <div class="brand">
      <div class="brand__name">Kentiva Day Spa</div>
      <div class="brand__tagline">Beauty, Health, Slimming</div>
    </div>

    <p class="intro">Come and relax</p>
    <h1 class="headline">Your Mind, Body<br>&amp; Soul will love it.</h1>
    <p class="offer">With one of our many packages that we have on offer.<br>Get treated with body wraps, herbal baths &amp; slimming,<br>or simply book for a normal treatment like a manicure...</p>
    <p class="closing">you deserve it!</p>

    <section class="services">
      <h2 class="services__title">Our services</h2>
      <ul class="services__list">
        <li class="services__item"><svg viewBox="0 0 16 16"><path d="M2 9 L6 13 L14 3" fill="none" stroke="var(--green)" stroke-width="3"/></svg>Relaxing Massages</li>
        <li class="services__item"><svg viewBox="0 0 16 16"><path d="M2 9 L6 13 L14 3" fill="none" stroke="var(--green)" stroke-width="3"/></svg>Deep Cleansing Facials</li>
        <li class="services__item"><svg viewBox="0 0 16 16"><path d="M2 9 L6 13 L14 3" fill="none" stroke="var(--green)" stroke-width="3"/></svg>Marvelous Manicures</li>
        <li class="services__item"><svg viewBox="0 0 16 16"><path d="M2 9 L6 13 L14 3" fill="none" stroke="var(--green)" stroke-width="3"/></svg>Soothing Pedicures</li>
        <li class="services__item"><svg viewBox="0 0 16 16"><path d="M2 9 L6 13 L14 3" fill="none" stroke="var(--green)" stroke-width="3"/></svg>Professional Waxing</li>
        <li class="services__item"><svg viewBox="0 0 16 16"><path d="M2 9 L6 13 L14 3" fill="none" stroke="var(--green)" stroke-width="3"/></svg>Sunbed Sessions</li>
      </ul>
    </section>

    <address class="address" style="font-style: normal;">
      Situated in Briarlea Park<br>
      Near many restaurants &amp; the Briarlea Park Guesthouse<br>
      16 Vennor Street, Briarlea Park, Oakhollow<br>
      Tel: (011) 555-0142 / (011) 555-0187<br>
      www.kentivadayspa.co.za
    </address>

    <div class="social">
      <div class="social__label">Find us on:</div>
      <div class="social__links">
        <span class="social__link"><span class="social__dot"></span>BriarleaSpa</span>
        <span class="social__link"><span class="social__dot"></span>@KentivaDaySpa</span>
      </div>
    </div>

    <p class="notice">Our rates can be viewed on your mobile phone as well. Simply visit the website address below and view our latest offers: www.kentivadayspa.co.za</p>
  </main>
</body>
</html>
```